Powerpoint Template with Pitch Slides, a logo, color palette and a few business diagrams

1) Powerpoint Template with Pitch Slides that are drafted in attached document
2) Color palette for Powerpoint Template. Think a blend between Bold and professional business
3) A Logo for Quilmo Enterprises (i like the icon that I attached)
4) A Quilmo Icon likely pulled from the logo
5) A few business diagrams like the ones attached. Dovenhulm, Lifecyle.

Industry/Entity Type

Applications, Finance

Font styles to use
Other font styles liked:
• Helvetica

```html
<!DOCTYPE html>
<html lang="en">
<head>
<meta charset="utf-8">
<title>Quilmo Enterprises – Presentation Template</title>
<link href="https://fonts.googleapis.com/css2?family=Oswald:wght@500;700&family=Roboto:wght@400;500;700&display=swap" rel="stylesheet">
<style>
:root{
  --yellow:#fcc502;
  --yellow-soft:#fff3a8;
  --orange:#f7a723;
  --ink:#231f20;
  --grey:#9a9a9a;
  --sheet:#e4e5e6;
  --white:#ffffff;
  --blue:#4a90c8;
  --band-fade:rgba(252,197,2,0);
  --band-glow:rgba(252,197,2,.6);
  --ink-glow:rgba(35,31,32,.45);
}
*{margin:0;padding:0;box-sizing:border-box}
html,body{width:814px;height:1200px;overflow:hidden;background:var(--sheet)}
body{position:relative;font-family:"Roboto",Helvetica,Arial,sans-serif;color:var(--ink)}
.slide{position:absolute;width:364px;height:205px;background:var(--white);overflow:hidden;box-shadow:3px 4px 6px rgba(0,0,0,.25)}
.col-a{left:44px}.col-b{left:418px}
.row-1{top:45px}.row-2{top:271px}.row-3{top:494px}.row-4{top:718px}.row-5{top:942px}
.abs{position:absolute}
.deco{position:absolute;left:0;top:0;width:364px;height:205px}

/* soft tone areas where the striped corner ornament sits */
.ornament{position:absolute}
.ornament.br{right:0;bottom:0;width:66px;height:82px;background:linear-gradient(to bottom right,var(--band-fade) 35%,var(--band-glow))}
.ornament.bl{left:0;bottom:0;width:106px;height:134px;background:linear-gradient(to bottom left,var(--band-fade) 35%,var(--band-glow))}
.ornament.ink-bl{left:0;bottom:0;width:56px;height:56px;background:linear-gradient(to bottom left,rgba(35,31,32,0) 30%,var(--ink-glow))}
.ornament.ink-br{right:0;bottom:0;width:56px;height:56px;background:linear-gradient(to bottom right,rgba(35,31,32,0) 30%,var(--ink-glow))}
.ornament.side-r{right:0;top:60px;width:30px;height:122px;background:linear-gradient(to right,var(--band-fade),var(--band-glow))}
.ornament.base{left:242px;bottom:0;width:82px;height:19px;background:linear-gradient(to bottom,var(--band-fade),var(--band-glow))}

.brand-mark{position:absolute;right:10px;top:10px;display:flex;align-items:center;gap:2px;font:700 5px "Roboto",Helvetica,sans-serif;color:var(--ink);letter-spacing:.2px}
.brand-mark i{display:block;width:5px;height:5px;background:var(--yellow)}
.heading{font-family:"Oswald",Impact,sans-serif;font-weight:700;font-size:11px;letter-spacing:-.1px;white-space:nowrap}
.heading .hl{color:var(--yellow)}
.heading .dk{font-family:"Roboto",Helvetica,sans-serif;font-weight:700}
.footer-url{position:absolute;left:16px;bottom:12px;font-size:3px;color:#555}
.footer-line{position:absolute;left:57px;right:30px;bottom:13px;height:.6px;background:var(--yellow)}
.footer-page{position:absolute;right:26px;bottom:11px;font-size:3px;color:#555}
.photo{position:absolute}

/* title slide */
.s-title{background:var(--yellow)}
.s-title .mark-square{left:170px;top:48px;width:24px;height:24px;background:var(--ink)}
.s-title h1{position:absolute;left:0;right:0;top:118px;text-align:center;font:700 18px "Oswald",Impact,sans-serif;letter-spacing:-.2px;color:var(--ink)}
.s-title .tag{position:absolute;left:0;right:0;top:142px;text-align:center;font-size:9px;color:var(--ink)}

/* photo title slide */
.s-photo .heading{position:absolute;left:0;right:0;top:34px;text-align:center;color:var(--white)}

/* toc */
.toc-title{position:absolute;left:154px;top:40px}
.toc-list{position:absolute;left:153px;top:69px;width:180px;list-style:none;font-size:5.2px;color:#333}
.toc-list li{display:flex;justify-content:space-between;height:8.7px}
.toc-list li span:last-child{width:20px}

/* timeline */
.tl-title{position:absolute;left:0;right:0;top:28px;text-align:center}
.tl-year{position:absolute;font:700 9.5px "Roboto",Helvetica,sans-serif}
.tl-block{position:absolute;width:42px}
.tl-block b{display:block;font:500 6px "Roboto",Helvetica,sans-serif;letter-spacing:.3px}
.tl-block p{font-size:3.8px;line-height:1.3;color:#333;margin-top:2px}

/* picture with content */
.pc-band{position:absolute;left:0;top:56px;width:172px;height:28px;background:var(--yellow)}
.pc-band .heading{position:absolute;right:7px;top:6px;color:var(--ink);font-size:10px}
.pc-band .heading .big{color:var(--white);font-size:13px}
.pc-sub{position:absolute;left:41px;top:90px;font-size:7.5px}
.pc-text{position:absolute;left:41px;top:106px;width:140px;font-size:3.8px;line-height:1.35;color:#333}

/* agenda */
.ag-title{position:absolute;left:0;right:0;top:27px;text-align:center}
.ag-cell{position:absolute;width:90px;height:50px}
.ag-cell .thumb{position:absolute;left:0;top:0;width:45px;height:31px}
.ag-cell b{position:absolute;left:48px;top:-1px;font:700 6px "Oswald",Impact,sans-serif;color:var(--blue)}
.ag-cell p{position:absolute;left:48px;top:11px;width:45px;font-size:4px;line-height:1.3;color:#333}

/* solution */
.so-title{position:absolute;left:18px;top:30px;font-size:11px}
.so-hub{position:absolute;left:82px;top:58px;width:84px;height:84px;border-radius:50%;background:var(--white);box-shadow:0 3px 8px rgba(0,0,0,.25)}
.so-hub div{position:absolute;left:7px;top:7px;width:70px;height:70px;border-radius:50%;background:var(--ink);display:flex;align-items:center;justify-content:center;color:var(--yellow);font:700 8px "Roboto",Helvetica,sans-serif}
.pill{position:absolute;height:24px;border-radius:12px;background:var(--yellow)}
.pill.or{background:var(--orange)}
.pill .num{position:absolute;left:3px;top:2px;width:20px;height:20px;border-radius:50%;background:#f0f0f0;border:1px solid var(--white);box-shadow:0 1px 3px rgba(0,0,0,.3);display:flex;align-items:center;justify-content:center;font-size:10px;color:#333}
.pill b{position:absolute;left:30px;top:3px;font-size:5px;color:var(--ink)}
.pill p{position:absolute;left:30px;top:9px;width:70px;font-size:2.8px;line-height:1.25;color:#333}

/* team */
.tm-ring{position:absolute;left:122px;top:30px;width:88px;height:88px;border-radius:50%;border:2.5px solid var(--ink)}
.tm-label{position:absolute;left:122px;top:62px;width:88px;text-align:center;line-height:1.1}
.tm-label span{display:block;font:700 10px "Oswald",Impact,sans-serif;color:var(--yellow)}
.tm-label strong{display:block;font:700 10px "Roboto",Helvetica,sans-serif}
.tm-note{position:absolute;width:72px}
.tm-note b{display:block;font:700 4.8px "Roboto",Helvetica,sans-serif;color:var(--yellow);line-height:1.15}
.tm-note p{font-size:3.9px;line-height:1.3;color:#333;margin-top:5px}
.tm-note.dark b{color:#666}

/* closing photo slide */
.cl-title{position:absolute;left:50px;top:88px;width:140px;text-align:center;line-height:1.1}
.cl-title span{display:block;font:700 16px "Oswald",Impact,sans-serif;color:var(--ink)}
.cl-title strong{display:block;font:700 15px "Roboto",Helvetica,sans-serif;color:var(--ink)}

/* quote */
.qt-band{position:absolute;left:0;top:0;width:364px;height:72px;background:var(--yellow)}
.qt-title{position:absolute;left:0;right:0;top:17px;text-align:center;color:var(--white)}
.qt-circle{position:absolute;top:47px;width:42px;height:42px;border-radius:50%;background:var(--white);border:2.5px solid var(--yellow)}
.qt-box{position:absolute;top:98px;width:111px;height:62px;background:var(--yellow-soft);padding:3px;font-size:3.9px;line-height:1.3;color:#333}
.qt-box::before{content:"";position:absolute;left:50%;top:-1px;margin-left:-5px;border:5px solid transparent;border-bottom:0;border-top-color:var(--yellow)}
</style>
</head>
<body>

<!-- 1 Title -->
<section class="slide s-title col-a row-1">
  <div class="ornament ink-bl" role="img" aria-label="Dark striped corner ornament"></div>
  <div class="ornament ink-br" role="img" aria-label="Dark striped corner ornament"></div>
  <div class="abs mark-square"></div>
  <h1>QUILMO ENTERPRISES</h1>
  <p class="tag">Look Forward with Quilmo</p>
</section>

<!-- 2 Title only -->
<section class="slide s-photo col-b row-1">
  <div class="photo" style="inset:0;background:radial-gradient(ellipse 30% 40% at 50% 60%,rgba(240,210,170,.75),rgba(240,210,170,0)),radial-gradient(ellipse 45% 35% at 25% 55%,rgba(70,170,120,.55),rgba(70,170,120,0)),radial-gradient(ellipse 40% 40% at 80% 50%,rgba(200,150,60,.5),rgba(200,150,60,0)),radial-gradient(ellipse 60% 30% at 50% 5%,rgba(160,110,90,.6),rgba(160,110,90,0)),linear-gradient(160deg,#10324a,#0b2236 55%,#1a2a22)" role="img" aria-label="Photo of a hand touching a digital fingerprint scanning interface"></div>
  <div class="brand-mark" style="color:#fff"><i></i>QUILMO</div>
  <h2 class="heading"><span class="hl">LOREM IPSUM IS SIMPLY</span> <span class="dk">TITLE ONLY</span></h2>
</section>

<!-- 3 Table of contents -->
<section class="slide col-a row-2">
  <div class="ornament bl" role="img" aria-label="Yellow striped corner ornament"></div>
  <div class="brand-mark"><i></i>QUILMO</div>
  <h2 class="heading toc-title"><span class="hl">TABLE OF</span> <span class="dk">CONTENTS</span></h2>
  <ul class="toc-list">
    <li><span>Lorem ipsum dolor sit amet, consectetur adipiscing elit ..............</span><span>1</span></li>
    <li><span>Lorem ipsum dolor sit.........................................................</span><span>5</span></li>
    <li><span>Lorem ipsum dolor sit amet, consectetur adipiscing elit,</span><span>7</span></li>
    <li><span>Lorem ipsum dolor sit amet,...................................................</span><span>8</span></li>
    <li><span>Lorem ipsum dolor sit amet, consectetur adipiscing elit,............</span><span>9-12</span></li>
    <li><span>Lorem ipsum dolor ...............................................................</span><span>13-15</span></li>
    <li><span>Lorem ipsum dolor sit amet, consectetur adipiscing elit,............</span><span>16</span></li>
    <li><span>Lorem ipsum dolor sit amet, consectetur ...................................</span><span>17</span></li>
    <li><span>Lorem ipsum dolor sit amet, consectetur adipiscing elit,............</span><span>18-25</span></li>
    <li><span>Lorem ipsum dolor sit amet, .................................................</span><span>26</span></li>
    <li><span>Lorem ipsum dolor sit amet, consectetur adipiscing elit,............</span><span>27</span></li>
    <li><span>Lorem ipsum dolor sit amet, consectetur adipiscing....................</span><span>28-29</span></li>
    <li><span>Lorem ipsum dolor..................................................................</span><span>30</span></li>
  </ul>
</section>

<!-- 4 Timeline -->
<section class="slide col-b row-2">
  <div class="ornament br" role="img" aria-label="Yellow striped corner ornament"></div>
  <svg class="deco" viewBox="0 0 364 205" aria-hidden="true">
    <g fill="#fcc502">
      <rect x="25" y="111" width="10" height="10"/><rect x="70" y="111" width="10" height="10"/>
      <rect x="115" y="111" width="10" height="10"/><rect x="136" y="111" width="10" height="10"/>
      <rect x="183" y="111" width="10" height="10"/><rect x="228" y="111" width="10" height="10"/>
      <rect x="250" y="111" width="10" height="10"/><rect x="302" y="111" width="10" height="10"/>
      <polygon points="318,105 345,116 318,127"/>
    </g>
    <g fill="#231f20">
      <rect x="48" y="111" width="10" height="10"/><rect x="93" y="111" width="10" height="10"/>
      <rect x="160" y="111" width="10" height="10"/><rect x="206" y="111" width="10" height="10"/>
      <rect x="273" y="111" width="10" height="10"/>
    </g>
    <g stroke="#231f20" stroke-width=".7">
      <line x1="49" y1="111" x2="49" y2="56"/><line x1="165" y1="111" x2="165" y2="56"/><line x1="278" y1="111" x2="278" y2="56"/>
      <line x1="102" y1="121" x2="102" y2="177"/><line x1="213" y1="121" x2="213" y2="177"/>
    </g>
    <g fill="#231f20"><circle cx="102" cy="177" r="1.5"/><circle cx="213" cy="177" r="1.5"/></g>
  </svg>
  <div class="brand-mark"><i></i>QUILMO</div>
  <h2 class="heading tl-title"><span class="hl">LOREM IPSUM IS SIMPLY</span> <span class="dk">TIMELINE</span></h2>
  <span class="tl-year" style="left:36px;top:125px">2016</span>
  <span class="tl-year" style="left:94px;top:97px">2017</span>
  <span class="tl-year" style="left:151px;top:125px">2018</span>
  <span class="tl-year" style="left:208px;top:97px">2019</span>
  <span class="tl-year" style="left:265px;top:125px">2020</span>
  <div class="tl-block" style="left:53px;top:58px"><b>TITLE</b><p>Lorem Ipsum is simply dummy text of the printing and typesetting industry.</p></div>
  <div class="tl-block" style="left:166px;top:58px"><b>TITLE</b><p>Lorem Ipsum is simply dummy text of the printing and typesetting industry.</p></div>
  <div class="tl-block" style="left:280px;top:58px"><b>TITLE</b><p>Lorem Ipsum is simply dummy text of the printing and typesetting industry.</p></div>
  <div class="tl-block" style="left:107px;top:138px"><b>TITLE</b><p>Lorem Ipsum is simply dummy text of the printing and typesetting industry.</p></div>
  <div class="tl-block" style="left:218px;top:138px"><b>TITLE</b><p>Lorem Ipsum is simply dummy text of the printing and typesetting industry.</p></div>
  <span class="footer-url">www.quilmoenterprises.com</span><span class="footer-line"></span><span class="footer-page">3</span>
</section>

<!-- 5 Picture with content -->
<section class="slide col-a row-3">
  <div class="ornament side-r" role="img" aria-label="Yellow diagonal stripe ornament"></div>
  <div class="ornament base" role="img" aria-label="Yellow vertical stripe ornament"></div>
  <div class="brand-mark"><i></i>QUILMO</div>
  <div class="pc-band"><h2 class="heading"><span>PICTURE WITH</span> <span class="big">CONTENT</span></h2></div>
  <p class="pc-sub">Lorem Ipsum is simply dummy text</p>
  <p class="pc-text">Lorem Ipsum is simply dummy text of the printing and typesetting industry. Lorem Ipsum has been the industry's standard dummy text Lorem Ipsum is simply dummy text of the printing and typesetting industry. Lorem Ipsum has been the industry's standard dummy textLorem Ipsum is simply dummy text of the printing and typesetting industry. Lorem Ipsum has been the industry's standard dummy textLorem Ipsum is simply dummy text of the printing and typesetting industry. Lorem Ipsum has been the industry's standard dummy textLorem Ipsum is simply dummy text of the printing and typesetting industry. Lorem Ipsum has been the industry's standard dummy text</p>
  <div class="photo" style="left:190px;top:41px;width:145px;height:71px;background:radial-gradient(ellipse 30% 35% at 52% 70%,rgba(225,180,150,.85),rgba(225,180,150,0)),radial-gradient(ellipse 25% 40% at 55% 20%,rgba(200,200,205,.6),rgba(200,200,205,0)),linear-gradient(100deg,#1e1e22,#4a4a50 30%,#2a2a2e 55%,#5a5a60 75%,#1e1e22)" role="img" aria-label="Photo of business people shaking hands and giving thumbs up"></div>
  <div class="photo" style="left:190px;top:115px;width:145px;height:71px;background:radial-gradient(ellipse 30% 40% at 35% 45%,rgba(70,70,75,.8),rgba(70,70,75,0)),radial-gradient(ellipse 25% 20% at 60% 65%,rgba(230,190,165,.7),rgba(230,190,165,0)),linear-gradient(180deg,#d9d6d0,#f3f1ee 55%,#c9c4bc)" role="img" aria-label="Photo of hands typing on a laptop at a desk"></div>
  <span class="footer-url">www.quilmoenterprises.com</span><span class="footer-line" style="right:40px"></span><span class="footer-page">3</span>
</section>

<!-- 6 Agenda -->
<section class="slide col-b row-3">
  <div class="ornament br" role="img" aria-label="Yellow striped corner ornament"></div>
  <svg class="deco" viewBox="0 0 364 205" aria-hidden="true">
    <g stroke="#cfcfcf" stroke-width=".6">
      <line x1="41" y1="107" x2="323" y2="107"/>
      <line x1="138" y1="55" x2="138" y2="160"/><line x1="234" y1="55" x2="234" y2="160"/>
    </g>
  </svg>
  <div class="brand-mark"><i></i>QUILMO</div>
  <h2 class="heading ag-title"><span class="hl">OUR BUSINESS</span> <span class="dk">AGENDA</span></h2>
  <div class="ag-cell" style="left:41px;top:55px"><div class="thumb" style="background:radial-gradient(ellipse 50% 40% at 60% 80%,#8a2a22,rgba(138,42,34,0)),linear-gradient(160deg,#6d90b0,#2e3e4e 60%,#1e2a34)" role="img" aria-label="Photo of a cargo ship in port"></div><b>TITLE</b><p>Lorem Ipsum is simply dummy text of the printing and typesetting industry.</p></div>
  <div class="ag-cell" style="left:141px;top:55px"><div class="thumb" style="background:radial-gradient(ellipse 40% 50% at 45% 55%,#3a4048,rgba(58,64,72,0)),linear-gradient(160deg,#b8c8d8,#8aa3bd 50%,#56606b)" role="img" aria-label="Photo of industrial machinery"></div><b>TITLE</b><p>Lorem Ipsum is simply dummy text of the printing and typesetting industry.</p></div>
  <div class="ag-cell" style="left:237px;top:55px"><div class="thumb" style="background:radial-gradient(ellipse 30% 60% at 55% 45%,#e8a51a,rgba(232,165,26,0)),linear-gradient(180deg,#9cc0e0,#6f9cc8 60%,#8a7a5a)" role="img" aria-label="Photo of a yellow construction crane"></div><b>TITLE</b><p>Lorem Ipsum is simply dummy text of the printing and typesetting industry.</p></div>
  <div class="ag-cell" style="left:41px;top:119px"><div class="thumb" style="background:radial-gradient(ellipse 50% 35% at 50% 40%,#f7a034,rgba(247,160,52,0)),linear-gradient(180deg,#e0591a,#a8361a 55%,#2a140c)" role="img" aria-label="Photo of an industrial plant at sunset"></div><b>TITLE</b><p>Lorem Ipsum is simply dummy text of the printing and typesetting industry.</p></div>
  <div class="ag-cell" style="left:141px;top:119px"><div class="thumb" style="background:radial-gradient(ellipse 60% 35% at 50% 78%,#f0b020,rgba(240,176,32,0)),linear-gradient(180deg,#9a968e,#5e5a54 50%,#c98a14)" role="img" aria-label="Photo of a factory hall with yellow machines"></div><b>TITLE</b><p>Lorem Ipsum is simply dummy text of the printing and typesetting industry.</p></div>
  <div class="ag-cell" style="left:237px;top:119px"><div class="thumb" style="background:radial-gradient(ellipse 35% 30% at 30% 25%,#f2f0ec,rgba(242,240,236,0)),radial-gradient(ellipse 30% 25% at 75% 25%,#e07a30,rgba(224,122,48,0)),linear-gradient(160deg,#cfc8bc,#8a5a3a 60%,#4a3222)" role="img" aria-label="Photo of engineers wearing hard hats"></div><b>TITLE</b><p>Lorem Ipsum is simply dummy text and typesetting industry.</p></div>
  <span class="footer-url">www.quilmoenterprises.com</span><span class="footer-line"></span><span class="footer-page">3</span>
</section>

<!-- 7 Solution -->
<section class="slide col-a row-4">
  <div class="ornament bl" role="img" aria-label="Yellow striped corner ornament"></div>
  <svg class="deco" viewBox="0 0 364 205" aria-hidden="true">
    <g fill="none" stroke="#f7a723" stroke-width="1.3">
      <polyline points="166,100 190,98 213,52 225,52"/>
      <polyline points="166,102 192,100 218,74 268,74"/>
      <polyline points="166,104 192,104 218,119 268,119"/>
      <polyline points="166,106 190,106 213,158 225,158"/>
    </g>
  </svg>
  <div class="brand-mark"><i></i>QUILMO</div>
  <h2 class="heading so-title"><span class="hl">LOREM IPSUM</span> <span class="dk">SOLUTION</span></h2>
  <div class="so-hub"><div>QUILMO</div></div>
  <div class="pill" style="left:170px;top:28px;width:116px"><span class="num">1</span><b>RETAIL SOLUTIONS</b><p>Lorem ipsum dolor sit amet, consectetur elit.</p></div>
  <div class="pill or" style="left:222px;top:62px;width:118px"><span class="num">2</span><b>ANALYTICS SOLUTIONS</b><p>Lorem ipsum dolor sit amet, consectetur elit.</p></div>
  <div class="pill" style="left:222px;top:106px;width:116px"><span class="num">3</span><b>FIELD SOLUTIONS</b><p>Lorem ipsum dolor sit amet, consectetur elit.</p></div>
  <div class="pill or" style="left:166px;top:145px;width:122px"><span class="num">4</span><b>ENERGY SOLUTIONS</b><p>Lorem ipsum dolor sit amet, consectetur elit.</p></div>
  <span class="footer-url">www.quilmoenterprises.com</span><span class="footer-line"></span><span class="footer-page">3</span>
</section>

<!-- 8 Team -->
<section class="slide col-b row-4">
  <div class="ornament br" role="img" aria-label="Yellow striped corner ornament"></div>
  <svg class="deco" viewBox="0 0 364 205" aria-hidden="true">
    <g fill="none" stroke="#9a9a9a" stroke-width=".8">
      <polyline points="57,41 104,41 124,57"/>
      <polyline points="57,81 104,81 123,86"/>
      <polyline points="57,140 122,140 138,111"/>
      <polyline points="289,34 228,34 204,52"/>
      <polyline points="289,95 240,95 210,83"/>
      <polyline points="289,140 222,140 190,113"/>
    </g>
    <g fill="#fcc502"><circle cx="124" cy="57" r="1.3"/><circle cx="204" cy="52" r="1.3"/><circle cx="138" cy="111" r="1.3"/><circle cx="190" cy="113" r="1.3"/></g>
    <g fill="#231f20"><circle cx="123" cy="86" r="1.3"/><circle cx="210" cy="83" r="1.3"/></g>
  </svg>
  <div class="brand-mark"><i></i>QUILMO</div>
  <div class="tm-ring"></div>
  <div class="tm-label"><span>LOREM IPSUM</span><strong>TEAM</strong></div>
  <div class="tm-note" style="left:30px;top:29px"><b>LOREM<br>IPSUM IS</b><p>Lorem ipsum dolor sit amet, consectetur adipiscing elit, sed do eiusmod tempor incididunt ut labore et dolore magna aliqua.</p></div>
  <div class="tm-note dark" style="left:30px;top:69px"><b>LOREM<br>IPSUM IS</b><p>Lorem ipsum dolor sit amet, consectetur adipiscing elit, sed do eiusmod tempor incididunt ut labore et dolore magna aliqua.</p></div>
  <div class="tm-note" style="left:30px;top:128px"><b>LOREM<br>IPSUM IS</b><p>Lorem ipsum dolor sit amet, consectetur adipiscing elit, sed do eiusmod tempor incididunt ut labore et dolore magna aliqua.</p></div>
  <div class="tm-note" style="left:245px;top:22px"><b>LOREM<br>IPSUM IS</b><p>Lorem ipsum dolor sit amet, consectetur adipiscing elit, sed do eiusmod tempor incididunt ut labore et dolore magna aliqua.</p></div>
  <div class="tm-note dark" style="left:245px;top:83px"><b>LOREM<br>IPSUM IS</b><p>Lorem ipsum dolor sit amet, consectetur adipiscing elit, sed do eiusmod tempor incididunt ut labore et dolore magna aliqua.</p></div>
  <div class="tm-note" style="left:245px;top:128px"><b>LOREM<br>IPSUM IS</b><p>Lorem ipsum dolor sit amet, consectetur adipiscing elit, sed do eiusmod tempor incididunt ut labore et dolore magna aliqua.</p></div>
  <span class="footer-url">www.quilmoenterprises.com</span><span class="footer-line"></span><span class="footer-page">3</span>
</section>

<!-- 9 Section photo -->
<section class="slide col-a row-5">
  <div class="photo" style="inset:0;background:radial-gradient(circle at 18% 28%,rgba(255,220,120,.8) 0,rgba(255,220,120,0) 16%),radial-gradient(circle at 48% 22%,rgba(255,200,90,.7) 0,rgba(255,200,90,0) 12%),radial-gradient(circle at 62% 80%,rgba(255,190,70,.75) 0,rgba(255,190,70,0) 14%),radial-gradient(circle at 88% 35%,rgba(255,215,110,.6) 0,rgba(255,215,110,0) 13%),radial-gradient(circle at 30% 85%,rgba(240,170,60,.6) 0,rgba(240,170,60,0) 12%),radial-gradient(ellipse at 45% 50%,#e0a63a 0%,#b8742a 40%,#6b3f1c 80%,#3a2412 100%)" role="img" aria-label="Photo of golden glittering bokeh lights"></div>
  <div class="ornament bl" role="img" aria-label="Yellow striped corner ornament"></div>
  <div class="brand-mark" style="color:#fff"><i></i>QUILMO</div>
  <div class="cl-title"><span>LOREM IPSUM</span><strong>SOLUTION</strong></div>
  <span class="footer-url" style="color:#fff">www.quilmoenterprises.com</span><span class="footer-line"></span><span class="footer-page" style="color:#fff">3</span>
</section>

<!-- 10 Quote -->
<section class="slide col-b row-5">
  <div class="qt-band"></div>
  <div class="ornament br" role="img" aria-label="Yellow striped corner ornament"></div>
  <div class="brand-mark"><i></i>QUILMO</div>
  <h2 class="heading qt-title">QUOTE SLIDE</h2>
  <div class="qt-circle" style="left:47px"></div>
  <div class="qt-circle" style="left:162px"></div>
  <div class="qt-circle" style="left:278px"></div>
  <p class="qt-box" style="left:12px">Lorem ipsum dolor sit amet, consectetur adipiscing elit, sed do eiusmod tempor incididunt ut labore et dolore magna aliqua. Lorem ipsum dolor sit amet, consectetur adipiscing elit, sed do eiusmod tempor incididunt ut labore et dolore magna aliqua.Lorem ipsum dolor sit amet, consectetur adipiscing elit, sed do eiusmod tempor incididunt ut labore et dolore magna aliqua.</p>
  <p class="qt-box" style="left:127px">Lorem ipsum dolor sit amet, consectetur adipiscing elit, sed do eiusmod tempor incididunt ut labore et dolore magna aliqua. Lorem ipsum dolor sit amet, consectetur adipiscing elit, sed do eiusmod tempor incididunt ut labore et dolore magna aliqua.Lorem ipsum dolor sit amet, consectetur adipiscing elit, sed do eiusmod tempor incididunt ut labore et dolore magna aliqua.</p>
  <p class="qt-box" style="left:243px">Lorem ipsum dolor sit amet, consectetur adipiscing elit, sed do eiusmod tempor incididunt ut labore et dolore magna aliqua. Lorem ipsum dolor sit amet, consectetur adipiscing elit, sed do eiusmod tempor incididunt ut labore et dolore magna aliqua.Lorem ipsum dolor sit amet, consectetur adipiscing elit, sed do eiusmod tempor incididunt ut labore et dolore magna aliqua.</p>
  <span class="footer-url">www.quilmoenterprises.com</span><span class="footer-line"></span><span class="footer-page">3</span>
</section>

</body>
</html>
```